Conference flyer

We need a flyer for a conference for the defence industry. The attached has been updated with new information using last years flyer. We would like something new and fresh. Please note the theme of the conference is 'a global environment'.

The final design should reflect the defence industry and manufacturing.

Defence

```html
<!DOCTYPE html>
<html lang="en">
<head>
<meta charset="utf-8">
<title>Defence Trade Controls Annual Flyer Design (Page 3 &amp; 4)</title>
<link rel="stylesheet" href="https://fonts.googleapis.com/css2?family=Caladea&family=Arimo:wght@400;700&family=Inter:wght@300;400;600;700&display=swap">
<style>
  :root {
    --ink: #1a1a1a;
    --muted: #3c3c3c;
    --accent: #29a9e0;
    --rule: #4fb8e6;
    --paper: #ffffff;
    --board: #ffffff;
    --banner-a: #c8102e;
    --banner-b: #1f3f99;
    --banner-c: #2e8b3a;
    --banner-d: #f3f3f3;
  }
  * { margin: 0; padding: 0; box-sizing: border-box; }
  html, body { width: 1200px; height: 1000px; overflow: hidden; background: var(--board); }
  body { position: relative; font-family: "Arimo", Arial, sans-serif; color: var(--ink); }

  .board-title {
    position: absolute; top: 70px; left: 0; width: 1200px; text-align: center;
    font-family: "Caladea", Georgia, serif; font-size: 20px; color: #111;
  }
  .page-label {
    position: absolute; top: 906px; width: 200px; text-align: center;
    font-family: "Caladea", Georgia, serif; font-size: 20px; color: #111;
  }
  .page-label--left { left: 218px; }
  .page-label--right { left: 782px; }

  .sheet {
    position: absolute; top: 117px; width: 540px; height: 765px; background: var(--paper);
    box-shadow: 1px 2px 5px rgba(0,0,0,.35), 0 0 1px rgba(0,0,0,.25);
  }
  .sheet--p3 { left: 48px; }
  .sheet--p4 { left: 612px; }

  .banner {
    position: absolute; left: 25px; top: 26px; width: 489px; height: 103px;
    background:
      linear-gradient(100deg, var(--banner-d) 0%, var(--banner-b) 14%, var(--banner-a) 30%, var(--banner-d) 42%, var(--banner-c) 52%, var(--banner-c) 62%, var(--banner-b) 72%, var(--banner-b) 100%);
  }

  .section-title {
    position: absolute; left: 25px; font-family: "Inter", sans-serif; font-weight: 300;
    font-size: 16.5px; color: var(--accent);
  }

  /* Agenda */
  .day { position: absolute; top: 185px; width: 240px; }
  .day--one { left: 11px; }
  .day--two { left: 283px; }
  .day-heading { font-family: "Inter", sans-serif; font-weight: 300; font-size: 13.5px; margin: 0 0 12px 14px; }
  .day--two .day-heading { margin-left: 0; }
  .day-heading b { font-weight: 700; }
  .session { display: grid; grid-template-columns: 78px 1fr; font-size: 8.6px; line-height: 12px; margin-bottom: 10px; }
  .day--two .session { grid-template-columns: 64px 1fr; }
  .session-time { color: var(--muted); }
  .session-title { font-weight: 700; }
  .session-note { display: block; font-weight: 400; font-style: italic; color: var(--muted); }
  .topics { list-style: none; margin-top: 2px; font-weight: 400; color: var(--muted); }
  .topics li { line-height: 14.6px; padding-left: 12px; position: relative; }
  .topics li::before { content: ">"; position: absolute; left: 0; color: var(--accent); }

  .footer-rule { position: absolute; left: 25px; width: 489px; top: 725px; border-top: 1px solid var(--rule); }
  .footer-text { position: absolute; top: 733px; font-size: 7px; color: var(--muted); }
  .sheet--p3 .footer-text { right: 26px; }
  .sheet--p4 .footer-text { left: 26px; }
  .footer-text span { margin: 0 4px; }

  /* Training */
  .block-title { position: absolute; left: 26px; font-family: "Inter", sans-serif; font-weight: 600; font-size: 12.5px; }
  .rule { position: absolute; left: 26px; width: 489px; border-top: 1px solid var(--rule); }
  .module-row { position: absolute; left: 26px; width: 450px; display: grid; grid-template-columns: 103px 1fr; font-size: 8.6px; line-height: 12px; color: var(--muted); }
  .module-row p { margin-bottom: 2px; }
  .module-row b { color: var(--ink); }
  .module-row .wrap { padding-left: 45px; display: block; }

  /* Prices */
  .price-table { position: absolute; left: 26px; top: 458px; width: 489px; border-collapse: collapse; font-size: 8.6px; }
  .price-table th { font-weight: 700; text-align: center; line-height: 12px; height: 36px; vertical-align: middle; border-bottom: 1px solid var(--rule); }
  .price-table td { text-align: center; color: var(--muted); border-bottom: 1px solid var(--rule); line-height: 12px; }
  .price-table td.item { text-align: left; font-weight: 700; color: var(--ink); }
  .price-table tr.single td { height: 32px; }
  .price-table tr.double td { height: 44px; }
  .price-table col.c-item { width: 121px; }
</style>
</head>
<body>
  <h1 class="board-title">Defence Trade Controls Annual Flyer Design (Page 3 &amp; 4)</h1>

  <section class="sheet sheet--p3">
    <div class="banner" role="img" aria-label="Photo of keyboard keys printed with national flags"></div>
    <h2 class="section-title" style="top:150px">Agenda</h2>

    <div class="day day--one">
      <h3 class="day-heading"><b>Day 1:</b> Tuesday, 2 June 2015</h3>
      <div class="session"><span class="session-time">0830 – 0900</span><span class="session-title">Registration</span></div>
      <div class="session"><span class="session-time">0900 – 0915</span><span class="session-title">Chair’s Welcome and<br>Opening Address</span></div>
      <div class="session"><span class="session-time">0915 – 0950</span><span class="session-title">Australian Legislative Changes</span></div>
      <div class="session"><span class="session-time">0950 – 1030</span><span class="session-title">Export Control Reform – Next Steps</span></div>
      <div class="session"><span class="session-time">1030 – 1100</span><span class="session-title">Morning Tea and Networking</span></div>
      <div class="session"><span class="session-time">1100 – 1145</span><span class="session-title">Managing Multi-jurisdictional<br>Programs</span></div>
      <div class="session"><span class="session-time">1145 – 1230</span><span class="session-title">Country Focus: Japan</span></div>
      <div class="session"><span class="session-time">1230 – 1330</span><span class="session-title">Lunch</span></div>
      <div class="session"><span class="session-time">1330 – 1400</span><span class="session-title">Export Control Reform and<br>FMS, CoA Management</span></div>
      <div class="session"><span class="session-time">1400 – 1430</span><span class="session-title">Country Focus: Singapore</span></div>
      <div class="session"><span class="session-time">1430 – 1500</span><span class="session-title">Customs Trusted Trader Program</span></div>
      <div class="session"><span class="session-time">1500 – 1530</span><span class="session-title">Afternoon Tea and Networking</span></div>
      <div class="session"><span class="session-time">1530 – 1645</span><span class="session-title">Industry Best Practice<span class="session-note">Panel Led by: Paul Hendry</span></span></div>
      <div class="session"><span class="session-time">1645 – 1730</span><span class="session-title">Day One Wrap Up</span></div>
      <div class="session"><span class="session-time">1730</span><span class="session-title">Reception</span></div>
    </div>

    <div class="day day--two">
      <h3 class="day-heading"><b>Day 2:</b> Wednesday, 3 June 2015</h3>
      <div class="session"><span class="session-time">0900 – 0910</span><span class="session-title">Chair’s Welcome Back</span></div>
      <div class="session"><span class="session-time">0910 – 0950</span><span class="session-title">Best Practice Compliance</span></div>
      <div class="session"><span class="session-time">0950 – 1030</span><span class="session-title">Compliance Case Study</span></div>
      <div class="session"><span class="session-time">1030 – 1100</span><span class="session-title">Morning Tea and Networking</span></div>
      <div class="session"><span class="session-time">1100 – 1130</span><span class="session-title">Practical Management of<br>Export Control Reform</span></div>
      <div class="session"><span class="session-time">1130 – 1200</span><span class="session-title">EAR Exceptions – The Good,<br>The Bad and The Ugly</span></div>
      <div class="session"><span class="session-time">1200 – 1245</span><span class="session-title">Country Focus: European Union</span></div>
      <div class="session"><span class="session-time">1245 – 1345</span><span class="session-title">Lunch and Networking</span></div>
      <div class="session"><span class="session-time">1345 – 1500</span><span class="session-title">Export Control –<br>Round Table Discussions
        <ul class="topics">
          <li>Dual National Exemptions</li>
          <li>Understanding ‘Specially Designed’<br>Deminimis</li>
          <li>Re-exports Under EAR</li>
          <li>US Trade Co-operation Treaty</li>
          <li>Securing Your Supply Chain</li>
        </ul></span></div>
      <div class="session"><span class="session-time">1500 – 1530</span><span class="session-title">Conference Q&amp;A and Wrap Up</span></div>
      <div class="session"><span class="session-time">1530</span><span class="session-title">Conference Close</span></div>
    </div>

    <div class="footer-rule"></div>
    <p class="footer-text">Defence Trade Controls Annual Conference<span></span>3</p>
  </section>

  <section class="sheet sheet--p4">
    <div class="banner" role="img" aria-label="Photo of keyboard keys printed with national flags"></div>
    <h2 class="section-title" style="top:150px">4 x Half Day Pre and Post Training Sessions</h2>

    <h3 class="block-title" style="top:185px">Pre Conference Training Modules</h3>
    <div class="rule" style="top:209px"></div>
    <div class="module-row" style="top:220px">
      <span>Monday, 1 June 2015</span>
      <div><p><b>Module 1:</b> Export Controls for Beginners – Helping Beginners to Make the Best of<span class="wrap">the Conference</span></p></div>
    </div>
    <div class="rule" style="top:253px"></div>

    <h3 class="block-title" style="top:278px">Post Conference Training Modules</h3>
    <div class="rule" style="top:302px"></div>
    <div class="module-row" style="top:313px">
      <span>Thursday, 4 June 2015</span>
      <div><p><b>Module 2:</b> Practical Management of Export Control Reform</p><p><b>Module 3:</b> Tips and Hints for Best Practice Compliance</p></div>
    </div>
    <div class="rule" style="top:349px"></div>
    <div class="module-row" style="top:359px">
      <span>Friday, 5 June 2015</span>
      <div><p><b>Module 4:</b> Making the Best of Commerce Exceptions</p></div>
    </div>
    <div class="rule" style="top:381px"></div>

    <h2 class="section-title" style="top:414px;left:26px">Conferences Prices (All prices include GST)</h2>

    <table class="price-table">
      <colgroup><col class="c-item"><col><col><col></colgroup>
      <thead>
        <tr><th></th><th>Super Earlybird<br>(Prior 31 December 2014)</th><th>Earlybird<br>(Prior 31 March 2015)</th><th>Standard Pricing</th></tr>
      </thead>
      <tbody>
        <tr class="single"><td class="item">Conference Only</td><td>$1,095</td><td>$1,195</td><td>$1,295</td></tr>
        <tr class="double"><td class="item">Training Module (ea)<br>(With Conference)</td><td>$350</td><td>$399</td><td>$450</td></tr>
        <tr class="single"><td class="item">Training Module (ea) Only</td><td>$399</td><td>$450</td><td>$495</td></tr>
      </tbody>
    </table>

    <div class="footer-rule"></div>
    <p class="footer-text">4<span></span>Defence Trade Controls Annual Conference</p>
  </section>

  <p class="page-label page-label--left">Page 3</p>
  <p class="page-label page-label--right">Page 4</p>
</body>
</html>
```